Quadrawell - Human Capital Consultancy Business Cards

We need a business card design for a new professional services consulting company which is focused on People, Performance, Profit. Hence the company name "Quadrawell Pty Ltd". We intend to work with organisations predominantly on achieving optimal business performance through it's people. Developing both individual and organisational capability through effective learning and talent management strategies. We also plan to offer leadership programs which look at how people can utilise wellness, mindfulness and resilience to enable them and their teams to perform more effectively. We are looking for something quite dynamic, even sporty looking rather than a staid'professional services' look. Please see logo attached.

Industry/Entity Type

Leadership

```html
<!DOCTYPE html>
<html lang="en">
<head>
<meta charset="utf-8">
<title>Quadrawell Business Cards</title>
<link href="https://fonts.googleapis.com/css2?family=Ubuntu:wght@400;500;700&display=swap" rel="stylesheet">
<style>
  :root {
    --backdrop: #e6e8ec;
    --card-white: #ffffff;
    --card-black: #1c1c1c;
    --card-black-soft: #2e2e2e;
    --band-deep: #2a47b8;
    --band-light: #8fc3f0;
    --logo-grey: #7c7c7c;
    --accent-orange: #f28c1c;
    --text-dark: #3a3a3a;
    --text-light: #ffffff;
    --icon-blue: #3aa0e8;
  }
  * { margin: 0; padding: 0; box-sizing: border-box; }
  html, body { width: 1200px; height: 861px; overflow: hidden; }
  body {
    background: var(--backdrop);
    font-family: "Ubuntu", sans-serif;
    position: relative;
  }
  .card {
    position: absolute;
    top: 120px;
    width: 340px;
    height: 620px;
    background: var(--card-white);
    box-shadow: 0 10px 30px rgba(0,0,0,0.25);
    overflow: hidden;
  }
  .card--front { left: 220px; }
  .card--back { left: 640px; }
  .card__art { position: absolute; inset: 0; width: 100%; height: 100%; }
  .brand {
    position: absolute;
    left: 0; right: 0;
    display: flex;
    align-items: center;
    justify-content: center;
    gap: 10px;
  }
  .brand__dot {
    width: 26px; height: 26px;
    border-radius: 50%;
    background: var(--accent-orange);
  }
  .brand__name {
    font-weight: 500;
    font-size: 44px;
    color: var(--logo-grey);
    letter-spacing: -0.5px;
  }
  .tagline {
    position: absolute;
    left: 0; right: 0;
    text-align: center;
    font-size: 19px;
    color: var(--text-dark);
  }
  .card--front .brand { top: 235px; }
  .card--front .tagline { top: 318px; }
  .card--back .brand { top: 90px; }
  .card--back .tagline { top: 168px; }
  .web-address {
    position: absolute;
    left: 0; right: 0;
    top: 545px;
    text-align: center;
    font-weight: 700;
    font-size: 25px;
    color: var(--text-light);
  }
  .holder {
    position: absolute;
    left: 0; right: 0;
    top: 298px;
    text-align: center;
  }
  .holder__name {
    font-weight: 700;
    font-size: 34px;
    color: var(--accent-orange);
  }
  .holder__role {
    font-weight: 500;
    font-size: 20px;
    color: var(--text-light);
    margin-top: 4px;
  }
  .contacts {
    position: absolute;
    left: 38px;
    top: 400px;
    list-style: none;
  }
  .contacts__item {
    display: flex;
    align-items: center;
    gap: 12px;
    height: 38px;
    font-size: 18px;
    color: var(--text-light);
  }
  .contacts__icon { width: 26px; height: 26px; flex: none; }
</style>
</head>
<body>

  <section class="card card--front" aria-label="Card front">
    <svg class="card__art" viewBox="0 0 340 620" aria-hidden="true">
      <defs>
        <linearGradient id="bandFront" x1="0" x2="1" y1="0" y2="0">
          <stop offset="0" stop-color="var(--band-deep)"/>
          <stop offset="0.5" stop-color="var(--band-light)"/>
          <stop offset="1" stop-color="var(--band-deep)"/>
        </linearGradient>
        <linearGradient id="darkFront" x1="0" x2="0" y1="0" y2="1">
          <stop offset="0" stop-color="var(--card-black-soft)"/>
          <stop offset="1" stop-color="var(--card-black)"/>
        </linearGradient>
      </defs>
      <polygon points="0,0 340,0 340,70 170,118 0,70" fill="url(#darkFront)"/>
      <polygon points="0,70 170,118 340,70 340,96 170,144 0,96" fill="url(#bandFront)"/>
      <polygon points="0,470 170,424 340,470 340,496 170,450 0,496" fill="url(#bandFront)"/>
      <polygon points="0,496 170,450 340,496 340,620 0,620" fill="url(#darkFront)"/>
    </svg>
    <div class="brand"><span class="brand__dot"></span><span class="brand__name">Quadrawell</span></div>
    <p class="tagline">Talent • Growth • Results</p>
    <p class="web-address">www.quadrawell.com</p>
  </section>

  <section class="card card--back" aria-label="Card back">
    <svg class="card__art" viewBox="0 0 340 620" aria-hidden="true">
      <defs>
        <linearGradient id="bandBack" x1="0" x2="1" y1="0" y2="0">
          <stop offset="0" stop-color="var(--band-deep)"/>
          <stop offset="0.5" stop-color="var(--band-light)"/>
          <stop offset="1" stop-color="var(--band-deep)"/>
        </linearGradient>
        <linearGradient id="darkBack" x1="0" x2="0" y1="0" y2="1">
          <stop offset="0" stop-color="var(--card-black)"/>
          <stop offset="1" stop-color="var(--card-black-soft)"/>
        </linearGradient>
      </defs>
      <polygon points="0,248 170,202 340,248 340,274 170,228 0,274" fill="url(#bandBack)"/>
      <polygon points="0,274 170,228 340,274 340,620 0,620" fill="url(#darkBack)"/>
      <rect x="0" y="582" width="340" height="20" fill="url(#bandBack)"/>
    </svg>
    <div class="brand"><span class="brand__dot"></span><span class="brand__name">Quadrawell</span></div>
    <p class="tagline">Talent • Growth • Results</p>
    <div class="holder">
      <p class="holder__name">Name Surname</p>
      <p class="holder__role">Position</p>
    </div>
    <ul class="contacts">
      <li class="contacts__item">
        <svg class="contacts__icon" viewBox="0 0 26 26" aria-hidden="true">
          <circle cx="13" cy="13" r="11.5" fill="none" stroke="var(--icon-blue)" stroke-width="2"/>
          <path d="M9 8 l3 0 l1 3 l-2 1.5 q1.5 3 3.5 3.5 l1.5 -2 l3 1 l0 3 q-7 0 -10 -10z" fill="var(--icon-blue)"/>
        </svg>
        <span>+ 061 555 0198</span>
      </li>
      <li class="contacts__item">
        <svg class="contacts__icon" viewBox="0 0 26 26" aria-hidden="true">
          <circle cx="13" cy="13" r="11.5" fill="none" stroke="var(--icon-blue)" stroke-width="2"/>
          <rect x="7" y="9" width="12" height="8" fill="none" stroke="var(--icon-blue)" stroke-width="1.6"/>
          <polyline points="7,9 13,14 19,9" fill="none" stroke="var(--icon-blue)" stroke-width="1.6"/>
        </svg>
        <span>name@quadrawell.com</span>
      </li>
      <li class="contacts__item">
        <svg class="contacts__icon" viewBox="0 0 26 26" aria-hidden="true">
          <circle cx="13" cy="13" r="11.5" fill="none" stroke="var(--icon-blue)" stroke-width="2"/>
          <rect x="7" y="8" width="12" height="8" fill="none" stroke="var(--icon-blue)" stroke-width="1.6"/>
          <line x1="10" y1="19" x2="16" y2="19" stroke="var(--icon-blue)" stroke-width="1.6"/>
        </svg>
        <span>Quadrawell</span>
      </li>
      <li class="contacts__item">
        <svg class="contacts__icon" viewBox="0 0 26 26" aria-hidden="true">
          <circle cx="13" cy="13" r="11.5" fill="none" stroke="var(--icon-blue)" stroke-width="2"/>
        </svg>
        <span>www.quadrawell.com</span>
      </li>
    </ul>
  </section>

</body>
</html>
```